Accounting / taxation / finance frim needs a half size banner. It ll be an advantage if you desing f

We need a half a size (234 x 60) vertical stand banner design for our company based in Melbourne Australia.
We provide range of accounting, taxation services.
We also have strategic alliance with other law firm, migration firm and finance mortgage brokers.
The idea is to create a fully integrated service (one stop shop) for our clients.

We would like to see designs that match our existing website, brochure, business card, letter head and logo.

Our website is www.lumorvagroup.com.au... you may get all your contents from this website.

Our business name is LUMORVA Group. So the final design should deliver the message that we are Group of professionals that work hand in hand with our clients to achieve and go beyond clients need. The design should also convey the message that we are one stop shop to assist clients with their various needs.

Colors
3277b5
85acd3
886aae
b8a6cd
33b8a4
87d0c7
33a6d7
85cae6

Requirements
Must have
• LUMORVA Group Where guidance goes further
• LUMORVA Logo
• QEB Logo
• Levy Adviser Council Logo
• NRF Logo

```html
<!DOCTYPE html>
<html lang="en">
<head>
<meta charset="utf-8">
<title>LUMORVA Group – Stand Banner</title>
<link rel="stylesheet" href="https://fonts.googleapis.com/css2?family=Open+Sans:wght@400;600;700;800&display=swap">
<style>
  :root{
    --navy:#1f3166;
    --blue:#1577c5;
    --brand:#2b7fc4;
    --teal:#2bb3a0;
    --stage:#dcdcdc;
    --white:#ffffff;
    --ink:#1f3166;
  }
  *{margin:0;padding:0;box-sizing:border-box}
  html,body{width:1200px;height:1044px;overflow:hidden;background:var(--stage);font-family:"Open Sans",Arial,sans-serif}
  .banner{position:absolute;left:385px;top:32px;width:429px;height:980px;background:var(--white);overflow:hidden;box-shadow:0 6px 18px rgba(0,0,0,.18)}
  .city-backdrop{position:absolute;left:0;top:290px;width:429px;height:478px;background:linear-gradient(170deg,#ffffff 0%,#ffffff 25%,#eeeff1 55%,#dcdee2 85%,#e8e9eb 100%)}
  .banner-top{position:absolute;left:0;top:0;width:429px;height:310px}
  .headline{position:absolute;left:0;width:100%;text-align:center;color:var(--white);white-space:nowrap}
  .headline-name{top:62px;font-size:34px;font-weight:700;letter-spacing:.5px}
  .headline-tagline{top:104px;font-size:22px;font-weight:400}
  .brand-mark{position:absolute;left:155px;top:192px;width:118px;height:118px;border-radius:50%;background:var(--brand)}
  .brand-name{position:absolute;left:0;top:326px;width:100%;text-align:center;font-size:44px;font-weight:700;color:var(--ink);line-height:56px;white-space:nowrap}
  .services-title{position:absolute;left:0;top:419px;width:100%;text-align:center;font-size:18px;font-weight:700;color:var(--ink)}
  .services-rule{position:absolute;left:194px;top:447px;width:40px;height:3px;background:var(--teal)}
  .services-list{position:absolute;left:0;top:470px;width:100%;list-style:none;text-align:center}
  .services-list li{font-size:18px;font-weight:700;color:var(--ink);line-height:30px;white-space:nowrap}
  .accredit-strip{position:absolute;left:0;top:768px;width:100%;height:118px;background:var(--white)}
  .accredit-label{position:absolute;left:157px;top:0;width:114px;height:24px;background:var(--blue);color:var(--white);font-size:12px;font-weight:700;text-align:center;line-height:24px}
  .badge{position:absolute}
  .badge-nrf{left:52px;top:46px;width:40px;height:40px;border-radius:50%;background:#8a4fa3}
  .badge-qeb{left:176px;top:36px;width:130px;height:60px;background:var(--navy)}
  .badge-levy{left:324px;top:42px;width:44px;height:44px;border-radius:50%;background:#e9ecd6;border:2px solid #7bb342}
  .footer{position:absolute;left:0;top:886px;width:100%;height:94px;background:var(--navy);display:flex;align-items:center;justify-content:space-between;padding:0 14px}
  .contact{display:flex;align-items:center;gap:6px;color:var(--white);font-size:9px;line-height:12px;white-space:nowrap}
  .contact svg{flex:none}
</style>
</head>
<body>
  <main class="banner">
    <div class="city-backdrop" role="img" aria-label="Faint photograph of a tall glass office tower seen from below"></div>

    <svg class="banner-top" viewBox="0 0 429 310" aria-hidden="true">
      <polygon points="0,0 429,0 429,194 0,263" fill="#1f3166"/>
      <polygon points="0,263 429,194 429,214 0,298" fill="#1577c5"/>
    </svg>

    <h1 class="headline headline-name">LUMORVA GROUP</h1>
    <p class="headline headline-tagline">WHERE GUIDANCE GOES FURTHER</p>

    <div class="brand-mark" aria-hidden="true"></div>
    <div class="brand-name">LUMORVA</div>

    <h2 class="services-title">OUR SERVICES</h2>
    <div class="services-rule"></div>
    <ul class="services-list">
      <li>Migration</li>
      <li>Bookkeeping &amp; Payroll</li>
      <li>Finance &amp; Capital Raising</li>
      <li>Insolvency &amp; Restructuring</li>
      <li>Business Service &amp; Advisory</li>
      <li>CRB &amp; Corporate Secretarial</li>
      <li>Business Law &amp; Legal Services</li>
      <li>Management Consulting Services</li>
      <li>Taxation, Accounting &amp; Compliances</li>
    </ul>

    <section class="accredit-strip">
      <div class="accredit-label">ACCREDITED BY</div>
      <div class="badge badge-nrf" role="img" aria-label="NRF accreditation badge"></div>
      <div class="badge badge-qeb" role="img" aria-label="QEB accreditation badge"></div>
      <div class="badge badge-levy" role="img" aria-label="Levy Adviser Council registration badge"></div>
    </section>

    <footer class="footer">
      <div class="contact">
        <svg width="22" height="22" viewBox="0 0 26 26"><circle cx="13" cy="13" r="12" fill="none" stroke="#fff" stroke-width="1.3"/><path d="M9.5 8.5c.6-.6 1.3-.5 1.7.1l1 1.5c.3.5.2 1-.2 1.4l-.6.5c.6 1.2 1.4 2 2.6 2.6l.5-.6c.4-.4.9-.5 1.4-.2l1.5 1c.6.4.7 1.1.1 1.7-1.3 1.3-3.3.8-5.4-1.3s-2.6-4.1-1.3-5.4z" fill="#fff"/></svg>
        <span>Call us<br>1300 555 418</span>
      </div>
      <div class="contact">
        <svg width="22" height="22" viewBox="0 0 26 26"><circle cx="13" cy="13" r="12" fill="none" stroke="#fff" stroke-width="1.3"/><rect x="8" y="9.5" width="10" height="7" rx="1" fill="#fff"/><path d="M8.5 10l4.5 3.3 4.5-3.3" fill="none" stroke="#1f3166" stroke-width="1"/></svg>
        <span>Have any questions?<br>info@lumorvagroup.com.au</span>
      </div>
      <div class="contact">
        <svg width="22" height="22" viewBox="0 0 26 26"><circle cx="13" cy="13" r="12" fill="none" stroke="#fff" stroke-width="1.3"/><path d="M13 7a4 4 0 0 1 4 4c0 3-4 8-4 8s-4-5-4-8a4 4 0 0 1 4-4z" fill="#fff"/><circle cx="13" cy="11" r="1.5" fill="#1f3166"/></svg>
        <span>Level 4, 27 Harbour Lane<br>Melbourne, VIC 3000</span>
      </div>
    </footer>
  </main>
</body>
</html>
```